Harborvale Ventures brochure for Investment partnership, young harold pembly

We need a brochure design to attract new investors for our investing partnership Called Harborvale Ventures. We are based in New Orleans, La. We primarily invest in stocks, bonds, and crypto but venture out into other categories as well. We would like to see designs with the black and gold like our logo. The final design should say new, fresh, sleek, tech, and honorable. BROUCHURE WILL BE 4 pages.or one folded sheet a paparer if that makes sense.
Updates

A chart showing Harborvale Ventures gains since 2019 28.6 percent and the TR 400 gAINS 7.1 PERCENT

Target Market(s)

Probable Investors

Industry/Entity Type

Financial Planning

Colors

Designer to choose only greyscale colors for use in the design.

Requirements
Must have
• Black and Gold accent. Stock market feel. Sleek, High tech, innovative, Intellgent design.
Nice to have
• Page colors possibly black.
Should not have
• Boring, Old school,

```html
<!DOCTYPE html>
<html lang="en">
<head>
<meta charset="utf-8">
<title>Harborvale Ventures Brochure</title>
<link href="https://fonts.googleapis.com/css2?family=Montserrat:wght@300;400;500;600;700;800;900&display=swap" rel="stylesheet">
<style>
  :root {
    --backdrop: #e3e3e5;
    --paper: #ffffff;
    --paper-soft: #f6f6f6;
    --ink: #1a1a1a;
    --ink-soft: #555555;
    --charcoal: #2a2a2a;
    --gold: #c9a631;
    --photo-dark: #3a3a3a;
    --photo-mid: #8a8a8a;
    --photo-light: #d2d2d2;
  }
  * { box-sizing: border-box; margin: 0; padding: 0; }
  html, body { width: 1200px; height: 2700px; overflow: hidden; }
  body {
    background: var(--backdrop);
    font-family: "Montserrat", sans-serif;
    color: var(--ink);
    position: relative;
  }
  .stage { position: absolute; left: 0; width: 1200px; height: 900px; }
  .stage--cover { top: 0; }
  .stage--outside { top: 900px; border-top: 1px solid #d6d6d8; }
  .stage--inside { top: 1800px; border-top: 1px solid #d6d6d8; }

  .page {
    position: absolute;
    width: 470px; height: 620px;
    background: var(--paper);
    overflow: hidden;
    box-shadow: 0 10px 30px rgba(0,0,0,0.12);
  }

  .brand {
    position: absolute;
    font-family: "Montserrat", sans-serif;
    font-weight: 600;
    color: var(--gold);
    letter-spacing: 1px;
    text-transform: uppercase;
    white-space: nowrap;
  }

  /* Front cover */
  .cover .brand { right: 34px; top: 56px; font-size: 17px; }
  .cover .photo { position: absolute; left: 0; top: 95px; width: 470px; height: 300px; }
  .cover-text { position: absolute; left: 40px; top: 420px; width: 400px; }
  .cover-title {
    font-weight: 900; font-size: 27px; line-height: 1.0;
    color: var(--gold); text-transform: uppercase;
  }
  .cover-sub { font-weight: 600; font-size: 15px; line-height: 1.25; margin-top: 8px; }
  .rule { width: 58px; height: 2px; background: var(--ink); margin: 12px 0 10px; }
  .cover-tag { font-weight: 400; font-size: 12px; color: var(--ink-soft); }
  .cover-web { font-weight: 700; font-size: 12px; margin-top: 14px; }
  .cover-web span { color: var(--gold); }

  /* Back cover */
  .back { background: var(--charcoal); color: #e8e8e8; }
  .about { position: absolute; left: 38px; top: 60px; width: 210px; }
  .about-title {
    color: var(--gold); font-weight: 700; font-size: 10.5px;
    line-height: 1.3; text-transform: uppercase;
  }
  .about-body { font-size: 8.5px; line-height: 1.75; margin-top: 10px; color: #cfcfcf; }
  .contact { position: absolute; left: 38px; bottom: 60px; }
  .back .brand { position: static; font-size: 13px; display: block; margin-bottom: 14px; }
  .contact-title { font-weight: 700; font-size: 14px; color: #fff; margin-bottom: 10px; }
  .contact-row { display: flex; align-items: center; gap: 10px; font-size: 10px; margin-top: 7px; color: #e6e6e6; }
  .contact-row svg { width: 12px; height: 12px; flex: none; }

  /* Inside spread */
  .inside-left { background: var(--paper-soft); }
  .intro { position: absolute; left: 36px; top: 48px; width: 400px; font-weight: 700; font-size: 11.5px; line-height: 1.5; }
  .intro p + p { margin-top: 10px; }
  .inside-left .photo { position: absolute; left: 0; top: 196px; width: 470px; height: 330px; }
  .inside-left .brand { left: 36px; bottom: 36px; font-size: 13px; }

  .inside-right { background: var(--paper); }
  .top-band { position: absolute; left: 0; top: 26px; width: 470px; height: 16px; background: var(--ink); }
  .inside-right .photo { position: absolute; left: 0; top: 70px; width: 170px; height: 330px; }
  .steps { position: absolute; left: 196px; top: 76px; width: 250px; }
  .steps-title { font-weight: 700; font-size: 19px; color: var(--gold); margin-bottom: 14px; }
  .step { position: relative; padding-left: 34px; font-size: 8.5px; line-height: 1.6; color: var(--ink-soft); margin-bottom: 18px; }
  .step-num {
    position: absolute; left: 0; top: 0;
    width: 22px; height: 22px; border-radius: 50%;
    background: var(--ink); color: #fff;
    font-size: 8px; font-weight: 700;
    display: flex; align-items: center; justify-content: center;
  }
  .step-line { position: absolute; left: 206px; top: 128px; width: 1px; height: 214px; background: #bdbdbd; }
  .footer { position: absolute; right: 26px; bottom: 40px; display: flex; align-items: center; gap: 3px; }
  .footer-web {
    background: var(--ink); color: #fff;
    font-size: 8px; padding: 3px 10px; letter-spacing: 0.3px;
  }
  .footer-bar { width: 3px; height: 15px; background: var(--ink); }
  .spine { position: absolute; top: 0; width: 1px; height: 620px; background: rgba(0,0,0,0.08); }
</style>
</head>
<body>

<section class="stage stage--cover">
  <article class="page cover" style="left:365px; top:140px;">
    <div class="brand">Harborvale Ventures</div>
    <svg class="photo" viewBox="0 0 470 300" role="img" aria-label="Black and white photograph of a historic cathedral and iron fence on a narrow old street">
      <defs>
        <linearGradient id="coverPhotoA" x1="0" y1="0" x2="1" y2="1">
          <stop offset="0" stop-color="var(--photo-mid)"/>
          <stop offset="0.5" stop-color="var(--photo-dark)"/>
          <stop offset="1" stop-color="var(--photo-light)"/>
        </linearGradient>
      </defs>
      <polygon points="0,50 470,10 470,300 0,300" fill="url(#coverPhotoA)"/>
      <line x1="140" y1="38" x2="470" y2="10" stroke="var(--gold)" stroke-width="3"/>
    </svg>
    <div class="cover-text">
      <h1 class="cover-title">Become a partner<br>and build</h1>
      <p class="cover-sub">Generational wealth by investing in the<br>stock market</p>
      <div class="rule"></div>
      <p class="cover-tag">A first of its kind Investment Club</p>
      <p class="cover-web">www.<span>harborvaleventures</span>.com</p>
    </div>
  </article>
</section>

<section class="stage stage--outside">
  <article class="page back" style="left:130px; top:140px;">
    <div class="about">
      <h2 class="about-title">About Harborvale Ventures and General Partner</h2>
      <p class="about-body">Harborvale Ventures was founded in 2019 by General Partner Marcus Thibault with a group economic empowerment mission. Marcus Thibault has invested in stocks since a teenager, received his BA in economics from Bayou State University and is currently attending Gulf Coast University.</p>
    </div>
    <div class="contact">
      <span class="brand">Harborvale Ventures</span>
      <h3 class="contact-title">CONTACT US</h3>
      <div class="contact-row">
        <svg viewBox="0 0 12 12"><path d="M2.5 1 L4.5 1 L5.3 3.6 L4 4.6 Q5 7 7.4 8 L8.4 6.7 L11 7.5 L11 9.5 Q11 11 9.5 11 Q1 10.5 1 2.5 Q1 1 2.5 1 Z" fill="var(--gold)"/></svg>
        <span>555-014-2290</span>
      </div>
      <div class="contact-row">
        <svg viewBox="0 0 12 12"><rect x="0.5" y="2" width="11" height="8" fill="var(--gold)"/><path d="M0.5 2 L6 6.5 L11.5 2" stroke="var(--charcoal)" stroke-width="1" fill="none"/></svg>
        <span>info@harborvaleventures.com</span>
      </div>
      <div class="contact-row">
        <svg viewBox="0 0 12 12"><circle cx="6" cy="6" r="5" fill="none" stroke="var(--gold)" stroke-width="1.2"/><ellipse cx="6" cy="6" rx="2.2" ry="5" fill="none" stroke="var(--gold)" stroke-width="1"/><line x1="1" y1="6" x2="11" y2="6" stroke="var(--gold)" stroke-width="1"/></svg>
        <span>www.harborvaleventures.com</span>
      </div>
    </div>
  </article>
  <article class="page cover" style="left:600px; top:140px;">
    <div class="brand">Harborvale Ventures</div>
    <svg class="photo" viewBox="0 0 470 300" role="img" aria-label="Black and white photograph of a historic cathedral and iron fence on a narrow old street">
      <defs>
        <linearGradient id="coverPhotoB" x1="0" y1="0" x2="1" y2="1">
          <stop offset="0" stop-color="var(--photo-mid)"/>
          <stop offset="0.5" stop-color="var(--photo-dark)"/>
          <stop offset="1" stop-color="var(--photo-light)"/>
        </linearGradient>
      </defs>
      <polygon points="0,50 470,10 470,300 0,300" fill="url(#coverPhotoB)"/>
      <line x1="140" y1="38" x2="470" y2="10" stroke="var(--gold)" stroke-width="3"/>
    </svg>
    <div class="cover-text">
      <h1 class="cover-title">Become a partner<br>and build</h1>
      <p class="cover-sub">Generational wealth by investing in the<br>stock market</p>
      <div class="rule"></div>
      <p class="cover-tag">A first of its kind Investment Club</p>
      <p class="cover-web">www.<span>harborvaleventures</span>.com</p>
    </div>
  </article>
</section>

<section class="stage stage--inside">
  <article class="page inside-left" style="left:130px; top:140px;">
    <div class="intro">
      <p>If you are receiving this brochure its because someone sees you as a person that doesn't want to just work and pay bills. Your someone who wants to build real generational wealth.</p>
      <p>Not throw schemes but the using the greatest wealth builder available. The stock market.</p>
    </div>
    <svg class="photo" viewBox="0 0 470 330" role="img" aria-label="Black and white photograph of a vintage streetcar on a palm-lined city avenue">
      <defs>
        <linearGradient id="streetcarPhoto" x1="0" y1="0" x2="1" y2="1">
          <stop offset="0" stop-color="var(--photo-light)"/>
          <stop offset="0.45" stop-color="var(--photo-dark)"/>
          <stop offset="1" stop-color="var(--photo-mid)"/>
        </linearGradient>
      </defs>
      <rect width="470" height="330" fill="url(#streetcarPhoto)"/>
    </svg>
    <div class="brand">Harborvale Ventures</div>
    <div class="spine" style="right:0;"></div>
  </article>
  <article class="page inside-right" style="left:600px; top:140px;">
    <div class="top-band"></div>
    <svg class="photo" viewBox="0 0 170 330" role="img" aria-label="Continuation of the streetcar avenue photograph with palm trees and buildings">
      <defs>
        <linearGradient id="streetcarPhotoRight" x1="0" y1="0" x2="1" y2="1">
          <stop offset="0" stop-color="var(--photo-mid)"/>
          <stop offset="1" stop-color="var(--photo-light)"/>
        </linearGradient>
      </defs>
      <rect width="170" height="330" fill="url(#streetcarPhotoRight)"/>
    </svg>
    <div class="step-line"></div>
    <div class="steps">
      <h2 class="steps-title">How it works</h2>
      <div class="step"><span class="step-num">01</span>Make initial deposit. The general partner will invest in stocks, bonds and other investment vehicles on your behalf.</div>
      <div class="step"><span class="step-num">02</span>There is no upfront fees. The general partner will guarantee a 5 percent return and will work for free on your behalf until that is achieved. After the 5 percent return on the dollars invested the limited partner will receive 80 percent and the general partner will receive 20 percent of every dollar gained.</div>
      <div class="step"><span class="step-num">03</span>As the return and investments multiply the interests begins to compound annually. The legal partner legally owns shares of stock within the club and may redeem once a year or let money continue to earn interest.</div>
    </div>
    <div class="footer">
      <div class="footer-web">www.harborvaleventures.com</div>
      <div class="footer-bar"></div>
      <div class="footer-bar"></div>
    </div>
  </article>
</section>

</body>
</html>
```